Styling of small website for mid-sized Engineering and Manufacturing company

We need the styling for a professional website for a company wich delivers: engineering, manufacturing, assembling, servicing and prototyping. (typically, they produce complex devices in limited series (1-100 pieces. The client comes with an idea and they translate it into design and device).
We have already made a wire-frame, but need a style (colors, fonts, H1, H2, paragraphs, margins, padding etc).
The style must :
- express profession attitude (world of engineering)
- have a fresh, modern look
- be sober (enough (white) space between the elements
The style must also be able to be used in a RWD. At this moment the logo (just letters) uses a green color (#4C6E33), but it isn't an obligation to use the exact same color (even not the 'green' color itself if you think another color is better for the site).
Target Market(s)
engineering and production
Industry/Entity Type
It Company
Coding
Coded - Design and coding required
Number of Pages Required
5+ page

```html
<!DOCTYPE html>
<html lang="en">
<head>
<meta charset="utf-8">
<title>KAVEX – Engineering &amp; Manufacturing</title>
<link rel="stylesheet" href="https://fonts.googleapis.com/css2?family=Open+Sans:wght@400;600;700;800&display=swap">
<style>
  :root {
    --green: #3dab4c;
    --green-dark: #228a31;
    --blue: #3d6fb8;
    --orange: #db9226;
    --purple: #8e50c4;
    --link: #5b8fd6;
    --bg: #f2f2f2;
    --text: #222;
    --rule: #cfcfcf;
    --white: #fff;
  }
  * { box-sizing: border-box; margin: 0; padding: 0; }
  html, body { width: 1200px; height: 1000px; overflow: hidden; }
  body {
    background: var(--bg);
    font-family: "Open Sans", Arial, sans-serif;
    color: var(--text);
    position: relative;
  }
  .logo {
    position: absolute; left: 128px; top: 8px;
    font-size: 46px; font-weight: 800; color: var(--green); letter-spacing: 1px;
  }
  .main-nav {
    position: absolute; left: 467px; top: 18px; width: 604px; height: 39px;
    background: var(--green); display: flex;
  }
  .main-nav a {
    color: var(--white); text-decoration: none; font-weight: 700; font-size: 18px;
    line-height: 39px; padding: 0 12.5px;
  }
  .main-nav a.is-active { background: var(--green-dark); padding: 0 14px; }
  .intro { position: absolute; left: 131px; top: 106px; width: 950px; }
  .intro h1 { font-size: 27px; font-weight: 700; color: var(--green); line-height: 38px; }
  .intro p { font-size: 17px; line-height: 25.5px; margin-left: 3px; }
  .services {
    position: absolute; left: 172px; top: 259px; display: flex;
    box-shadow: 0 2px 4px rgba(0,0,0,.25);
  }
  .service { display: flex; flex-direction: column; }
  .service-photo { height: 167px; }
  .service-label {
    height: 49px; line-height: 47px; text-align: center; color: var(--white);
    font-size: 24px; font-weight: 400;
  }
  .service--engineering { width: 231px; }
  .service--engineering .service-label { background: var(--blue); }
  .service--engineering .service-photo { background: linear-gradient(135deg, #d8d8d8, #5a5a5a 70%, #2a2a2a); }
  .service--prototyping { width: 196px; }
  .service--prototyping .service-label { background: var(--orange); }
  .service--prototyping .service-photo { background: linear-gradient(160deg, #2b2b2b, #8a8a8a 50%, #d9d9d9); }
  .service--assembly { width: 210px; }
  .service--assembly .service-label { background: var(--purple); }
  .service--assembly .service-photo { background: linear-gradient(120deg, #bdbdbd, #6e6e6e 60%, #202020); }
  .service--servicing { width: 215px; }
  .service--servicing .service-label { background: var(--green); }
  .service--servicing .service-photo { background: linear-gradient(200deg, #e0e0e0, #7a7a7a 55%, #333); }
  .summary {
    position: absolute; left: 129px; top: 510px; width: 950px;
    font-size: 17px; line-height: 25.5px;
  }
  .summary strong { color: var(--link); font-weight: 700; }
  .showcase { position: absolute; left: 129px; top: 600px; width: 650px; }
  .showcase h2 { font-size: 27px; font-weight: 700; color: var(--green); line-height: 36px; }
  .showcase-photo {
    position: absolute; left: 0; top: 45px; width: 256px; height: 171px;
    background: linear-gradient(180deg, #c9c4bd 0%, #9a948d 45%, #4a4a4c 75%, #e0b98c 100%);
    box-shadow: 0 2px 4px rgba(0,0,0,.25);
  }
  .showcase p {
    position: absolute; left: 273px; top: 40px; width: 375px;
    font-size: 17px; line-height: 25.4px;
  }
  .reasons {
    position: absolute; left: 799px; top: 608px; height: 214px; width: 290px;
    border-left: 3px solid var(--rule); padding-left: 14px;
  }
  .reasons h3 { font-size: 21px; font-weight: 700; color: var(--green); line-height: 29px; margin-top: -6px; }
  .reasons ul { list-style: none; margin-top: 24px; }
  .reasons li {
    display: flex; align-items: center; gap: 9px;
    font-size: 18px; font-weight: 600; line-height: 35px;
  }
  .site-footer {
    position: absolute; left: 129px; top: 897px; width: 941px; height: 86px;
    background: var(--green); color: var(--white);
  }
  .social { position: absolute; left: 14px; top: 14px; display: flex; gap: 14px; }
  .social span {
    display: flex; align-items: center; gap: 6px; font-size: 15px; font-weight: 700;
  }
  .social i { width: 14px; height: 14px; background: var(--white); display: block; }
  .footer-col { position: absolute; top: 8px; font-size: 15px; line-height: 22px; }
  .footer-col h4 { font-size: 18px; font-weight: 700; line-height: 26px; }
  .footer-col--contact { left: 315px; }
  .footer-col--sales { left: 480px; }
  .footer-col--rnd { left: 722px; }
  .footer-col p { margin-left: 2px; }
</style>
</head>
<body>
  <header>
    <div class="logo">KAVEX</div>
    <nav class="main-nav">
      <a class="is-active" href="#">Home</a>
      <a href="#">Services</a>
      <a href="#">Portfolio</a>
      <a href="#">News</a>
      <a href="#">About Kavex</a>
      <a href="#">Contact</a>
    </nav>
  </header>

  <section class="intro">
    <h1>Technological solutions from idea to product</h1>
    <p>Lorem ipsum dolor sit amet, consectetur adipiscing elit. Proin facilisis mi nec massa volutpat ultrices. Donec mollis arcu eu mauris blandit, in egestas urna eleifend. Morbi a finibus ligula, vitae molestie orci. Mauris sit amet leo lorem. Nullam nec ante eu nisl facilisis volutpat. Duis a urna ac quam accumsan dapibus nec sit nid.</p>
  </section>

  <section class="services">
    <div class="service service--engineering">
      <div class="service-photo" role="img" aria-label="Desk with technical drawings, keyboard and a hand on a mouse"></div>
      <div class="service-label">Engineering</div>
    </div>
    <div class="service service--prototyping">
      <div class="service-photo" role="img" aria-label="Close-up of a machined gear rack"></div>
      <div class="service-label">Prototyping</div>
    </div>
    <div class="service service--assembly">
      <div class="service-photo" role="img" aria-label="Hands assembling a device on a workbench"></div>
      <div class="service-label">Assembleren</div>
    </div>
    <div class="service service--servicing">
      <div class="service-photo" role="img" aria-label="Technician repairing a circuit board with a multimeter"></div>
      <div class="service-label">Servicing</div>
    </div>
  </section>

  <p class="summary">Mauris lorem arcu, ultricies vel mauris in, maximus accumsan metus. Phasellus sed lacinia libero. Nullam vel massa mauris. <strong>Engineering, prototype, (serie)productie, en service</strong> onder een dak. Maximus vel arcu vel.</p>

  <section class="showcase">
    <h2>Showcase Client X</h2>
    <div class="showcase-photo" role="img" aria-label="Client working on a laptop on a sofa in an office lounge"></div>
    <p>Vestibulum ac cursus ex. Nam et lectus at est tempor semper eget ac libero. Ut non iaculis diam. Mauris finibus diam id dolor laoreet scelerisque a vel diam. Sed odio orci, lacinia id nibh id, volutpat hendrerit elit. Nulla scelerisque eleifend magna sit amet vulputate. Mauris diam id dolar orci.</p>
  </section>

  <aside class="reasons">
    <h3>Waroom klantem voor ons kiezen</h3>
    <ul>
      <li><svg width="18" height="16" viewBox="0 0 18 16"><path d="M1.5 8.5 L6.5 13.5 L16.5 2" fill="none" stroke="#3dab4c" stroke-width="3.5"/></svg>Al 4.251 abonnees</li>
      <li><svg width="18" height="16" viewBox="0 0 18 16"><path d="M1.5 8.5 L6.5 13.5 L16.5 2" fill="none" stroke="#3dab4c" stroke-width="3.5"/></svg>1 keer per maand</li>
      <li><svg width="18" height="16" viewBox="0 0 18 16"><path d="M1.5 8.5 L6.5 13.5 L16.5 2" fill="none" stroke="#3dab4c" stroke-width="3.5"/></svg>Exclusieve tips en promos</li>
    </ul>
  </aside>

  <footer class="site-footer">
    <div class="social">
      <span><i></i>Linkup</span>
      <span>Chirpr</span>
    </div>
    <div class="footer-col footer-col--contact">
      <h4>Contact Us</h4>
      <p>info@kavex.com<br>+32 456 78 90</p>
    </div>
    <div class="footer-col footer-col--sales">
      <h4>Our Sales Department</h4>
      <p>Street x<br>xxxxxx City (View Map)</p>
    </div>
    <div class="footer-col footer-col--rnd">
      <h4>R&amp;D and Production</h4>
      <p>Street X<br>xxxxxxx City (View Map)</p>
    </div>
  </footer>
</body>
</html>
```